Sleek business card design for digital agency.

Brief document attached for detailed description and inspiration. Looking for a minimalist sleek, cool, modern business card design.

Industry/Entity Type

Digital

```html
<!DOCTYPE html>
<html lang="en">
<head>
<meta charset="utf-8">
<title>Rivet Studio – Business Card</title>
<link href="https://fonts.googleapis.com/css2?family=Open+Sans:wght@400;600&display=swap" rel="stylesheet">
<style>
  :root {
    --backdrop: #2b2725;
    --card: #1c1c1d;
    --card-edge: #151516;
    --gloss: #3b3b3d;
    --mark: #4a4a4c;
    --text: #f2f2f2;
    --text-soft: #d6d6d6;
    --accent: #1f8fc9;
  }
  * { margin: 0; padding: 0; box-sizing: border-box; }
  html, body { width: 1200px; height: 716px; overflow: hidden; }
  body {
    background: var(--backdrop);
    font-family: "Open Sans", Arial, sans-serif;
    position: relative;
  }
  .card {
    position: absolute;
    background: var(--card);
    border: 1px solid var(--card-edge);
    border-radius: 4px;
  }
  .card-front {
    left: 100px; top: 215px;
    width: 500px; height: 286px;
    display: flex; align-items: center; justify-content: center; gap: 18px;
  }
  .brand-dot {
    width: 46px; height: 46px; border-radius: 50%;
    background: var(--gloss);
  }
  .brand-name {
    font-size: 54px; font-weight: 600; color: var(--gloss);
    letter-spacing: 1px;
  }
  .card-back {
    left: 720px; top: 108px;
    width: 286px; height: 500px;
    padding: 40px 30px 0;
    color: var(--text);
  }
  .back-brand {
    display: flex; align-items: center; gap: 10px;
    margin-bottom: 58px;
  }
  .back-brand .brand-dot { width: 22px; height: 22px; background: var(--mark); }
  .back-brand .brand-name { font-size: 20px; color: var(--mark); letter-spacing: 0.5px; }
  .person-name { font-size: 25px; font-weight: 400; letter-spacing: 0.3px; }
  .person-role { font-size: 13px; text-transform: uppercase; letter-spacing: 0.5px; color: var(--text-soft); margin-top: 4px; }
  .person-note { font-size: 14px; color: var(--text-soft); margin-top: 2px; }
  .divider {
    height: 2px; background: var(--accent);
    margin: 14px -30px 22px;
  }
  .contact-group { font-size: 14px; line-height: 1.45; color: var(--text-soft); margin-bottom: 12px; }
</style>
</head>
<body>
  <section class="card card-front">
    <span class="brand-dot"></span>
    <span class="brand-name">Rivet Studio</span>
  </section>

  <section class="card card-back">
    <div class="back-brand">
      <span class="brand-dot"></span>
      <span class="brand-name">Rivet Studio</span>
    </div>
    <h1 class="person-name">Daniel Hurst</h1>
    <p class="person-role">Marketing Director</p>
    <p class="person-note">Drink order: G&amp;T with cucumber</p>
    <div class="divider"></div>
    <div class="contact-group">
      <p>0400 128 406</p>
      <p>03 9000 4172</p>
      <p>dhurst@rivetstudio.com</p>
    </div>
    <div class="contact-group">
      <p>Level 2, 18 Kemp St</p>
      <p>Eastwood NSW 2000</p>
    </div>
    <div class="contact-group">
      <p>@dhurst82</p>
      <p>facebook.com/RivetStudio</p>
    </div>
  </section>
</body>
</html>
```